Business Card for Maplethorne Elder Keepers

I need a business card design for a very elite and personalized companion care company. We take care of the client at home with respect, dignity, and our full attention. The design should communicate a classic elegance and trust.

/Users/lorafenwick/Downloads/graphwellhub_121488_23943024_3826329_sourcefile

```html
<!DOCTYPE html>
<html lang="en">
<head>
<meta charset="utf-8">
<title>Maplethorne Elder Keepers – Business Card</title>
<link rel="stylesheet" href="https://fonts.googleapis.com/css2?family=Quattrocento:wght@400;700&display=swap">
<style>
  :root {
    --navy: #154f85;
    --navy-deep: #124a7c;
    --sky: #4fb3e3;
    --sky-bright: #2fb6ee;
    --ink: #3a3a3a;
    --paper: #f7f7f6;
    --backdrop: #e4e4e4;
  }
  * { box-sizing: border-box; margin: 0; padding: 0; }
  html, body { width: 1200px; height: 1200px; overflow: hidden; }
  body {
    background: var(--backdrop);
    font-family: "Quattrocento", Georgia, serif;
    position: relative;
  }
  .card {
    position: absolute;
    width: 711px;
    height: 416px;
    background: var(--paper);
    border-radius: 22px;
    overflow: hidden;
  }
  .card--front { left: 238px; top: 120px; }
  .card--back  { left: 231px; top: 645px; }

  .brand-name {
    position: absolute;
    color: var(--navy);
    font-weight: 400;
    text-transform: uppercase;
    line-height: 1;
    text-align: right;
  }
  .brand-name span { display: block; }
  .brand-name .line-main { font-size: 52px; letter-spacing: 1px; }
  .brand-name .line-sub { font-size: 34px; letter-spacing: 1.5px; margin-top: 8px; }

  .card--front .brand-name { left: 100px; top: 150px; width: 510px; }
  .card--back .brand-name { left: 42px; top: 58px; width: 445px; }
  .card--back .brand-name .line-main { font-size: 46px; }
  .card--back .brand-name .line-sub { font-size: 30px; }

  .accent-bar {
    position: absolute; left: 0; bottom: 0; height: 16px; width: 100%;
    display: flex;
  }
  .accent-bar .bar-dark { flex: 0 0 356px; background: var(--navy); }
  .accent-bar .bar-light { flex: 1; background: var(--sky); }

  .address {
    position: absolute; left: 43px; top: 192px;
    font-size: 17.5px; color: var(--ink); letter-spacing: 0.3px;
  }
  .contact-list {
    position: absolute; left: 43px; top: 226px;
    list-style: none; font-size: 17.5px; color: var(--ink);
  }
  .contact-list li { display: flex; align-items: center; height: 25px; }
  .contact-list svg { width: 16px; height: 16px; margin-right: 20px; fill: var(--navy); }

  .wave { position: absolute; left: 0; top: 0; width: 711px; height: 416px; }

  .person {
    position: absolute; right: 38px; top: 302px; text-align: right;
  }
  .person-name { font-size: 29px; color: var(--sky-bright); letter-spacing: 0.5px; }
  .person-title { font-size: 17px; color: #ffffff; margin-top: 6px; letter-spacing: 0.3px; }
</style>
</head>
<body>

<section class="card card--front">
  <h1 class="brand-name">
    <span class="line-main">Maplethorne</span>
    <span class="line-sub">Elder Keepers</span>
  </h1>
  <div class="accent-bar"><div class="bar-dark"></div><div class="bar-light"></div></div>
</section>

<section class="card card--back">
  <svg class="wave" viewBox="0 0 711 416" aria-hidden="true">
    <path fill="#124a7c" d="M0,375 C160,385 310,360 430,300 C530,250 610,218 711,208 L711,416 L0,416 Z"/>
    <path fill="none" stroke="#154f85" stroke-width="7" stroke-linecap="round"
          d="M60,342 C220,365 330,322 430,262 C530,202 620,188 711,184"/>
    <path fill="#2fb6ee" d="M0,322 C110,345 240,350 350,328 C260,358 120,364 0,352 Z"/>
  </svg>

  <h1 class="brand-name">
    <span class="line-main">Maplethorne</span>
    <span class="line-sub">Elder Keepers</span>
  </h1>

  <p class="address">418 Birchwell Lane Ashford Glen, FL 30112</p>
  <ul class="contact-list">
    <li>
      <svg viewBox="0 0 16 16"><path d="M1 5c0-2 3-3 7-3s7 1 7 3v1h-4V5H5v1H1z M3 7h10l1 7H2z M8 9a2 2 0 1 0 .01 0z"/></svg>
      555-014-2231
    </li>
    <li>
      <svg viewBox="0 0 16 16"><path d="M1 3h14v10H1z" /><path d="M1 3l7 6 7-6" fill="none" stroke="#f7f7f6" stroke-width="1.3"/></svg>
      lora@maplethornekeepers.com
    </li>
    <li>
      <svg viewBox="0 0 16 16"><circle cx="8" cy="8" r="7"/><path d="M1 8h14M8 1v14M3 4h10M3 12h10" stroke="#f7f7f6" stroke-width="0.9" fill="none"/><ellipse cx="8" cy="8" rx="3" ry="7" fill="none" stroke="#f7f7f6" stroke-width="0.9"/></svg>
      www.maplethornekeepers.com
    </li>
  </ul>

  <div class="person">
    <p class="person-name">Lora Fenwick</p>
    <p class="person-title">Managing Director</p>
  </div>
</section>

</body>
</html>
```